Flyer for teen fitness class at a physiotherapy clinic

We are a passionate Physiotherapy Clinic requiring a flyer to promote our new service a fitness class for teenagers, which is called Youth's FLX - Flexible Limber Xtra Power. The aim of the class is to prevents injuries in sports, improve sporting performance and provide safe activity for otherwise inactive teens. The aim of the flyer is to make people aware of this new service and interested in joining. Ideally the Flyer would incorporate blue colours. Our logo must be on the flier, and at least one or two of the photos provided. Our logo is provided in the attachments. Required information : Youth's FLX: Flexible Limber Xtra Power, times Mondays and Wednesdays 4 -5. Can be claimed on private health insurance. Expert advice to tailor a program to individual needs. For more information go www.rmpvq.com.au or phone 03)5871 6093.

Industry/Entity Type

Clinic

```html
<!DOCTYPE html>
<html lang="en">
<head>
<meta charset="utf-8">
<title>Youth's FLX – Flyer</title>
<link href="https://fonts.googleapis.com/css2?family=Didact+Gothic&family=Poiret+One&family=Bebas+Neue&display=swap" rel="stylesheet">
<style>
  :root {
    --teal: #1e6f80;
    --navy: #0e47a1;
    --sky: #4aa6ea;
    --ink: #1d3234;
    --ink-strong: #0c0c0c;
    --paper: #ffffff;
    --mist: #e2eaf4;
  }
  html, body { margin: 0; padding: 0; overflow: hidden; }
  body { width: 1200px; height: 850px; background: var(--paper); }
  .flyer {
    position: relative;
    width: 1200px;
    height: 850px;
    overflow: hidden;
    background: linear-gradient(160deg, var(--paper) 0%, #f3f6fb 45%, var(--mist) 100%);
  }
  .backdrop { position: absolute; inset: 0; }
  .class-line {
    font-family: "Didact Gothic", sans-serif;
    font-size: 20px;
    fill: var(--paper);
  }
  .athlete-photo {
    position: absolute;
    left: 0;
    top: 55px;
    width: 370px;
    height: 795px;
    clip-path: polygon(0 0, 295px 0, 295px 330px, 370px 420px, 370px 100%, 0 100%);
    background: linear-gradient(180deg, #c9b7a8 0%, #b9b9bd 35%, #6d7180 70%, #9a9ea6 100%);
  }
  .benefits {
    position: absolute;
    left: 318px;
    top: 64px;
    margin: 0;
    font-family: "Didact Gothic", sans-serif;
    color: var(--teal);
    font-size: 61px;
    line-height: 52px;
  }
  .benefits p { margin: 0 0 44px; white-space: nowrap; }
  .contact {
    position: absolute;
    left: 376px;
    top: 478px;
    width: 772px;
    text-align: center;
  }
  .contact-lead {
    margin: 0 0 0 80px;
    text-align: left;
    font-family: "Poiret One", sans-serif;
    font-size: 58px;
    line-height: 70px;
    color: var(--ink-strong);
  }
  .contact-web, .contact-or, .contact-phone {
    margin: 0;
    font-family: "Bebas Neue", sans-serif;
    color: var(--ink);
  }
  .contact-web { font-size: 82px; line-height: 88px; margin-left: 10px; }
  .contact-or { font-size: 80px; line-height: 70px; color: var(--ink-strong); margin-left: 10px; }
  .contact-phone { font-size: 118px; line-height: 112px; white-space: nowrap; text-align: left; }
  .contact-phone .label { color: var(--ink-strong); }
</style>
</head>
<body>
<main class="flyer">
  <svg class="backdrop" width="1200" height="850" viewBox="0 0 1200 850">
    <defs>
      <linearGradient id="frameTop" x1="0" y1="0" x2="1" y2="0">
        <stop offset="0" stop-color="#0e47a1"/>
        <stop offset="0.75" stop-color="#0e47a1" stop-opacity="0.15"/>
        <stop offset="1" stop-color="#0e47a1" stop-opacity="0"/>
      </linearGradient>
      <linearGradient id="frameSide" x1="0" y1="0" x2="0" y2="1">
        <stop offset="0" stop-color="#0e47a1"/>
        <stop offset="1" stop-color="#0e47a1" stop-opacity="0"/>
      </linearGradient>
      <linearGradient id="floor" x1="0" y1="0" x2="1" y2="1">
        <stop offset="0" stop-color="#dfe2e6"/>
        <stop offset="0.5" stop-color="#c3c7cc"/>
        <stop offset="1" stop-color="#a9adb3"/>
      </linearGradient>
    </defs>
    <rect class="frame-top" x="26" y="28" width="1000" height="7" fill="url(#frameTop)"/>
    <rect class="frame-side" x="26" y="28" width="8" height="430" fill="url(#frameSide)"/>
    <polygon class="floor" points="0,520 1200,335 1200,850 0,850" fill="url(#floor)"/>
    <polygon class="band-sky-upper" points="0,430 420,400 0,470" fill="#9ccbf2" opacity="0.7"/>
    <polygon class="band-navy" points="0,470 1200,282 1200,312 0,550" fill="var(--navy)"/>
    <polygon class="band-white" points="0,550 1200,312 1200,325 0,565" fill="#ffffff"/>
    <polygon class="band-sky" points="560,458 1200,318 1200,338 560,475" fill="var(--sky)"/>
    <text class="class-line" x="400" y="446" transform="rotate(-10 400 446)">Youth's FLX: Flexible Limber Xtra Power · Mondays &amp; Wednesdays 4–5pm</text>
  </svg>

  <div class="athlete-photo" role="img" aria-label="Photo of a smiling teenager in a cap and singlet training on a reformer machine"></div>

  <section class="benefits">
    <p>Can be claimed on private<br>Health Insurance</p>
    <p>Expert advice to tailor a program<br>to individual needs</p>
  </section>

  <section class="contact">
    <p class="contact-lead">For more information go</p>
    <p class="contact-web">www.rmpvq.com.au</p>
    <p class="contact-or">or</p>
    <p class="contact-phone"><span class="label">Phone</span> 03)5871 6093</p>
  </section>
</main>
</body>
</html>
```